shopfitters cards and stationery
Stationery
Project: shopfitters cards and stationery
shopfitters cards and stationery  - Construction
Creative Brief
Professional
Mark Pelling
Contracts Manager
7/24 Quarry Lane Wendale 4182
mark@fitwrightgroup.com.au
www.fitwrightgroup.com.au
Phone numbers and other details etc will change if you could use them for know that will be great. give me your best work :) Thanks

```html
<!DOCTYPE html>
<html lang="en">
<head>
<meta charset="utf-8">
<title>Fitwright Group – Business Card</title>
<link href="https://fonts.googleapis.com/css2?family=Josefin+Sans:wght@400;700&display=swap" rel="stylesheet">
<style>
  :root {
    --backdrop: #e9e7e3;
    --card: #ffffff;
    --brand-blue: #2a6fc9;
    --accent-violet: #5a4fb0;
    --text-dark: #3a3a44;
    --icon-fill: #6a5fc0;
    --mark-blue: #2f5fc4;
  }
  * { margin: 0; padding: 0; box-sizing: border-box; }
  html, body {
    width: 1200px; height: 902px; overflow: hidden;
    background: var(--backdrop);
    font-family: "Josefin Sans", "Helvetica Neue", Arial, sans-serif;
  }
  .card {
    position: absolute; left: 100px; top: 146px;
    width: 1000px; height: 610px;
    background: var(--card);
    box-shadow: 0 10px 30px rgba(0,0,0,0.12);
  }
  .brand-circle {
    position: absolute; left: 95px; top: 135px;
    width: 350px; height: 350px; border-radius: 50%;
    background: var(--mark-blue);
  }
  .wordmark {
    position: absolute; right: 70px; top: 58px;
    font-weight: 700; font-size: 52px; letter-spacing: 3px;
    color: var(--brand-blue); text-transform: uppercase; line-height: 1;
  }
  .details {
    position: absolute; right: 70px; top: 160px;
    text-align: right; font-variant: small-caps;
    color: var(--text-dark); letter-spacing: 2px;
  }
  .person-name {
    font-size: 30px; color: var(--accent-violet); margin-bottom: 8px;
  }
  .person-role { font-size: 24px; margin-bottom: 34px; }
  .contact-list { list-style: none; font-size: 22px; }
  .contact-list li {
    display: flex; justify-content: flex-end; align-items: center;
    gap: 12px; height: 32px;
  }
  .contact-list li.web-group { margin-top: 26px; }
  .contact-list .plain { padding-right: 30px; }
  .icon { width: 18px; height: 18px; flex: none; }
</style>
</head>
<body>
  <div class="card">
    <div class="brand-circle"></div>
    <div class="wordmark">Fitwright Group</div>

    <div class="details">
      <div class="person-name">Mark Pelling</div>
      <div class="person-role">Contracts Manager</div>
      <ul class="contact-list">
        <li>7/24 Quarry Lane
          <svg class="icon" viewBox="0 0 18 18"><circle cx="9" cy="9" r="9" fill="var(--icon-fill)"/><path d="M9 4a3 3 0 0 1 3 3c0 2.5-3 6-3 6s-3-3.5-3-6a3 3 0 0 1 3-3z" fill="#fff"/></svg>
        </li>
        <li class="plain">Wendale 4182</li>
        <li>07-3012-4470
          <svg class="icon" viewBox="0 0 18 18"><circle cx="9" cy="9" r="9" fill="var(--icon-fill)"/><path d="M5.5 5h2l1 2-1.2 1a6 6 0 0 0 2.7 2.7l1-1.2 2 1v2c-4.5 0-8-3.5-8-8z" fill="#fff"/></svg>
        </li>
        <li>0412-558-309
          <svg class="icon" viewBox="0 0 18 18"><circle cx="9" cy="9" r="9" fill="var(--icon-fill)"/><rect x="6.5" y="4" width="5" height="10" rx="1" fill="#fff"/></svg>
        </li>
        <li>07 3019 6621
          <svg class="icon" viewBox="0 0 18 18"><circle cx="9" cy="9" r="9" fill="var(--icon-fill)"/><rect x="5" y="7" width="8" height="6" fill="#fff"/><rect x="6.5" y="4" width="5" height="3" fill="#fff"/></svg>
        </li>
        <li class="web-group">mark@fitwrightgroup.com.au
          <svg class="icon" viewBox="0 0 18 18"><circle cx="9" cy="9" r="9" fill="var(--icon-fill)"/><rect x="4.5" y="6" width="9" height="6" fill="#fff"/><path d="M4.5 6l4.5 3.5L13.5 6" stroke="var(--icon-fill)" fill="none"/></svg>
        </li>
        <li>www.fitwrightgroup.com.au
          <svg class="icon" viewBox="0 0 18 18"><circle cx="9" cy="9" r="9" fill="var(--icon-fill)"/><circle cx="9" cy="9" r="4.5" fill="none" stroke="#fff"/><path d="M4.5 9h9M9 4.5v9" stroke="#fff"/></svg>
        </li>
      </ul>
    </div>
  </div>
</body>
</html>
```